Brisk Tutorium Website

We are looking for a new design of our website. The current website is www.brisktutorium.example. The company is the #1 pre-college math and science program in Orange County, CA. We would like to see designs that integrate our logo with a modern color scheme. We are also open for suggestions that could improve our logo. We would like a simple, minimal, clean, classy, and vibrant front-page user interface design that give the premium, modern, innovative, creative, and premier brand feel. We like the "New Retro Colors for the Web" as described here: http://www.pixel-layoutnook.example/en/layout-notes-2013/.

Target Market(s)

The target market is parents with K-12 students from a diverse population. Parents are well educated with family income > $150,000. Most of the decision makers are mothers from immigrate families: 30% Chinese, 30% Korean, 15% Indian, 24% White.

Industry/Entity Type

College

Requirements
Must have
• Must read our statement of differentiation at:
• http://brisktutorium.example/about-us
• Your design must be reflective of your understanding of the statements.
Nice to have
• The design should also be mobil friendly.
Should not have
• While most of our current classes are math, our company is expanding to include STEM (Science, Technology, Engineering, and Math) for gifted students. Therefore, the site should not be JUST a math education site.

```html
<!DOCTYPE html>
<html lang="en">
<head>
<meta charset="utf-8">
<title>Brisk Tutorium</title>
<link href="https://fonts.googleapis.com/css2?family=Open+Sans:ital,wght@0,400;0,600;1,400&display=swap" rel="stylesheet">
<style>
:root{
  --navy:#2e3191;
  --navy-text:#2a3190;
  --green:#8cc43f;
  --red:#ef4e52;
  --teal:#23b1c2;
  --amber:#fbb040;
  --grey-band:#efefef;
  --text:#4a4a4a;
  --muted:#9a9a9a;
  --white:#ffffff;
}
*{box-sizing:border-box;margin:0;padding:0}
html,body{width:978px;height:1200px;overflow:hidden;background:var(--white)}
body{position:relative;font-family:"Open Sans",Arial,sans-serif;color:var(--text)}

.site-header{position:absolute;top:0;left:0;width:978px;height:89px}
.brand{position:absolute;left:80px;top:22px;display:flex;align-items:center;gap:10px}
.brand-mark{width:26px;height:26px;border-radius:50%;background:var(--navy)}
.brand-name{font-size:26px;font-weight:400;color:var(--navy-text);letter-spacing:.3px}
.login-btn{position:absolute;left:693px;top:8px;width:43px;height:18px;border-radius:3px;background:linear-gradient(#fff,#e6e6e6);box-shadow:0 2px 3px rgba(0,0,0,.25);font-size:7px;text-align:center;line-height:18px;color:#333}
.search{position:absolute;left:745px;top:7px;width:141px;height:19px;border:1px solid #cfcfcf;border-radius:2px;background:#f8f8f8;display:flex;align-items:center}
.search-drop{width:14px;height:100%;border-right:1px solid #ddd;display:flex;align-items:center;justify-content:center}
.search-field{flex:1;font-size:6.5px;color:#7aa0c8;padding-left:6px}
.search-go{width:18px;height:15px;margin-right:2px;background:linear-gradient(#7fcf4a,#3e9c22);border-radius:2px;display:flex;align-items:center;justify-content:center}

.main-nav{position:absolute;top:89px;left:0;width:978px;height:36px;background:var(--navy)}
.main-nav ul{list-style:none;position:absolute;left:0;top:0;height:36px;width:978px}
.main-nav li{position:absolute;top:0;line-height:36px;font-size:11.5px;color:var(--white);letter-spacing:.2px}

.hero{position:absolute;top:125px;left:0;width:978px;height:462px;background:linear-gradient(100deg,#3a2c24 0%,#8a6a55 25%,#d7b59c 50%,#a98a77 72%,#cfc8c4 100%)}
.hero-caption{position:absolute;left:80px;top:328px;width:820px;height:94px;background:rgba(60,60,60,.45);color:var(--white);text-align:center;font-size:17px;line-height:25px;padding-top:24px}
.hero-arrow{position:absolute;top:365px}

.feature-row{position:absolute;top:548px;left:80px;width:820px;height:360px;display:grid;grid-template-columns:204px 206px 205px 205px}
.feature{padding:20px 8px 0 16px;color:var(--white);overflow:hidden}
.feature h2{font-size:18px;font-weight:400;margin-bottom:18px}
.feature-photo{width:170px;height:81px;border:3px solid var(--white);margin-bottom:24px}
.feature p,.feature li{font-size:10.6px;line-height:15px;letter-spacing:-.25px}
.feature .date{color:#1d1d1d;margin-bottom:4px}
.feature .entry{margin-bottom:12px}
.feature a{color:#111;text-decoration:none}
.news{background:var(--green)}
.elearn{background:var(--red)}
.register{background:var(--teal)}
.schedule{background:var(--amber);padding-left:14px}
.schedule ul{list-style:none}
.schedule li{position:relative;padding-left:12px}
.schedule li::before{content:"";position:absolute;left:0;top:6px;width:4px;height:4px;background:var(--white)}

.info-band{position:absolute;top:908px;left:0;width:978px;height:243px;background:var(--grey-band)}
.info-band h2{font-size:18px;font-weight:400;color:var(--navy-text);margin-bottom:18px}
.about{position:absolute;left:97px;top:32px;width:372px}
.about p{font-size:10.6px;line-height:15px;letter-spacing:-.2px;color:#444}
.about a{color:var(--navy-text);text-decoration:none}
.newsletter{position:absolute;left:508px;top:32px;width:180px}
.newsletter .field{height:29px;background:var(--white);margin-bottom:10px;font-size:11px;font-style:italic;color:#a8a8c8;padding:7px 14px}
.newsletter .submit{display:inline-block;background:var(--navy);color:var(--white);font-size:11.5px;padding:6px 15px;margin-top:2px}
.contact{position:absolute;left:732px;top:32px;width:200px}
.contact address{font-size:10.5px;line-height:14px;font-style:italic;color:#444;letter-spacing:-.2px}
.contact a{color:var(--navy-text);text-decoration:none}
.contact .links{margin-top:14px;font-size:10.8px;line-height:14px;font-style:italic;letter-spacing:-.2px}

.site-footer{position:absolute;top:1151px;left:0;width:978px;height:49px}
.copyright{position:absolute;left:87px;top:21px;font-size:7.5px;color:var(--muted)}
.footer-links{position:absolute;left:612px;top:21px;display:flex;gap:14px;font-size:7.5px;color:var(--muted)}
.social{position:absolute;left:818px;top:11px;display:flex;gap:6px}
.social span{width:22px;height:22px;border-radius:50%;background:#d6d6d6;display:block}
</style>
</head>
<body>

<header class="site-header">
  <div class="brand">
    <span class="brand-mark"></span>
    <span class="brand-name">Brisk Tutorium</span>
  </div>
  <div class="login-btn">login</div>
  <div class="search">
    <span class="search-drop"><svg width="5" height="4" viewBox="0 0 5 4"><path d="M0 0h5L2.5 4z" fill="#6a8fc0"/></svg></span>
    <span class="search-field">Search</span>
    <span class="search-go"><svg width="9" height="9" viewBox="0 0 10 10"><circle cx="4" cy="4" r="2.8" fill="none" stroke="#1f4a10" stroke-width="1.3"/><path d="M6 6l3 3" stroke="#1f4a10" stroke-width="1.5"/></svg></span>
  </div>
</header>

<nav class="main-nav">
  <ul>
    <li style="left:104px">HOME</li>
    <li style="left:175px">ABOUT US</li>
    <li style="left:268px">MATHS</li>
    <li style="left:343px">PHYSICS</li>
    <li style="left:426px">CHEMISTRY</li>
    <li style="left:527px">BIOLOGY</li>
    <li style="left:611px">SCIENCE FAIR</li>
    <li style="left:729px">FALL 2013</li>
    <li style="left:817px">RESULTS</li>
  </ul>
</nav>

<section class="hero" role="img" aria-label="Photo of four smiling students leaning together">
  <div class="hero-caption">We provide after-school enrichment programs in math, physics, chemistry, biology,<br>and computer science, mentor middle...</div>
  <svg class="hero-arrow" style="left:80px" width="10" height="18" viewBox="0 0 10 18"><path d="M8 2L2 9l6 7" fill="none" stroke="#fff" stroke-width="2"/></svg>
  <svg class="hero-arrow" style="left:888px" width="10" height="18" viewBox="0 0 10 18"><path d="M2 2l6 7-6 7" fill="none" stroke="#fff" stroke-width="2"/></svg>
</section>

<section class="feature-row">
  <article class="feature news">
    <h2>News &amp; Events</h2>
    <div class="feature-photo" role="img" aria-label="Photo of a student browsing library shelves" style="background:linear-gradient(#c9c9c9,#5e5e5e)"></div>
    <div class="entry">
      <p class="date">February 12th 2013</p>
      <p>Lorem ipsum dolor sep sit aet sed lorem ipsum onectur aispicing lipe consectetur...</p>
    </div>
    <div class="entry">
      <p class="date">February 12th 2013</p>
      <p>Lorem ipsum dolor sep sit aet sed lorem ipsum onectur aispicing lipe consectetur...</p>
    </div>
  </article>
  <article class="feature elearn">
    <h2>E-learning</h2>
    <div class="feature-photo" role="img" aria-label="Photo of a teacher reviewing work with a student" style="background:linear-gradient(90deg,#e8e6e2,#6b5a50)"></div>
    <p>Students have access to learning resources, can review classroom materials, download homework solutions, view grade reports, and share knowledge with classmates in a protected environment. Parents will be able to monitor their children's learning progress and participate in forum discussions related to development. <a href="#">Click here to log in</a></p>
  </article>
  <article class="feature register">
    <h2>Registration</h2>
    <div class="feature-photo" role="img" aria-label="Photo of a student resting on a stack of books" style="background:linear-gradient(90deg,#d9e6ee,#f2f2f2)"></div>
    <p>The early registration deadline for returning students and summer camp participants is August 15. The open registration period is from August 15, 2013 - August 31, 2013.&nbsp; To register, clink on the program title below</p>
    <p style="margin-top:17px">To learn more about class schedule, qualification, waiting list, and other information <a href="#">click here.</a></p>
  </article>
  <article class="feature schedule">
    <h2>Scheduler</h2>
    <div class="feature-photo" role="img" aria-label="Photo of a campus building against a blue sky" style="background:linear-gradient(#3d6fc0,#8fb2e6)"></div>
    <ul>
      <li>Winter Session: Dec 3, 2013-Feb 23, 2013 (Holiday Break from Dec 23, 2013 - Jan 5, 2014)</li>
      <li>Winter Olympiads Bootcamp:Dec 26 - 30, 2013</li>
      <li>Spring Session: Mar 3, 2014 - May 11, 2014</li>
      <li>Jump Start Math Classes</li>
      <li>Biology Olympiad Summer Camp</li>
      <li>Student Registration : Schedule a qualifying exam</li>
    </ul>
  </article>
</section>

<section class="info-band">
  <div class="about">
    <h2>Why Brisk Tutorium for Gifted Youth?</h2>
    <p>In 2006, Brisk Tutorium for Gifted Youth was the first academy to offer advanced math problem solving to gifted students in Orange County. With its roots in the Irvine math community and locations proximate to Lakeside State University and Meridian College, Brisk Tutorium for Gifted Youth combines California Standardized Mathematics Curriculum with math competitions and problem solving to help gifted students to discover their passion, develop their skills, and fulfill their college dreams.&nbsp; To learn more about our philosophy, history, statement of differentiation, and approach to gifted education, <a href="#">click here.</a></p>
  </div>
  <div class="newsletter">
    <h2>Newsletter</h2>
    <div class="field">Name</div>
    <div class="field">Email</div>
    <span class="submit">Register me</span>
  </div>
  <div class="contact">
    <h2>Contact us</h2>
    <address>
      Brisk Tutorium for Gifted Youth<br>
      812 Scholar Lane, Suite 140<br>
      Irvine, CA 92600-0140<br>
      Phone: (555) 014-2211<br>
      Fax:&nbsp;&nbsp;&nbsp;&nbsp; (555) 014-0888<br>
      e-mail: <a href="#">info@brisktutorium.example</a>
    </address>
    <div class="links">
      <a href="#">Maps to Brisk Tutorium, Irvine</a><br>
      <a href="#">Directions to Brisk Tutorium, Irvine</a>
    </div>
  </div>
</section>

<footer class="site-footer">
  <p class="copyright">2013 Brisk Tutorium&nbsp;&nbsp; All Right Reserved</p>
  <div class="footer-links"><span>FAQs</span><span>Terms Of Use</span><span>Privacy Policy</span><span>Careers</span></div>
  <div class="social"><span></span><span></span><span></span></div>
</footer>

</body>
</html>
```